Ledger Paladin Powerpoint with Marshal Voltanic Type Theme

Need powerpoint template with matching colors and different slide options. Logo and colors to be used can be found at ledgerpaladinx.com. Want brightly colored slide deck that is readable form the back of a room, but highlights colors. I will be incorporating Tribbo into the slides to gamify my presentations.

Target Market(s)

Tech

Industry/Entity Type

IT, specifically database, but crossing over to mental health in IT, important note this is not for a company, this is just for a professional building a brand

Font styles to use
Sans Serif

Colors
0054AA
0677BA
7BADD7
CADEEF
E8F1F8
EB3D1F
EC4F4E
F09395
F8D3D4
FCEDEE

Requirements
Must have
• My Logo in the bottom corner, front page, a thank your page, question page, content page, content page with two columns, content page with graphs, and icons to be used in the primary colors of the logos, About Me Page, Break Slides, Demo break slide
Should not have
• Lighter shades of colors, I want to pop out where colors are used, I want spacing and font size to be readable from the back of a room, most likely black text and white background

```html
<!DOCTYPE html>
<html lang="en">
<head>
<meta charset="utf-8">
<title>Ledger Paladin Presentation Template</title>
<link href="https://fonts.googleapis.com/css2?family=Archivo+Black&family=Arimo:wght@400;700&family=Oswald:wght@500&display=swap" rel="stylesheet">
<style>
  :root {
    --navy: #0b3f97;
    --deep: #06114a;
    --brand-blue: #0054aa;
    --mid-blue: #0677ba;
    --sky: #7badd7;
    --cyan: #72e2f7;
    --bar-mid: #3092d0;
    --bar-dark: #2f6ab8;
    --red: #e3192b;
    --ink: #222;
    --body: #333;
    --white: #fff;
    --stage: #8c8c8c;
    --pill-line: #9a9a9a;
  }
  * { box-sizing: border-box; margin: 0; padding: 0; }
  html, body { width: 1200px; height: 1078px; overflow: hidden; }
  body {
    background: radial-gradient(ellipse at center, #a6a6a6 0%, var(--stage) 70%, #7a7a7a 100%);
    font-family: "Arimo", Arial, sans-serif;
    position: relative;
  }
  .slide {
    position: absolute;
    width: 547px; height: 307px;
    background: var(--white);
    overflow: hidden;
    box-shadow: 0 10px 18px rgba(0,0,0,.35);
  }
  .col-left { left: 44px; }
  .col-right { left: 609px; }
  .row-1 { top: 59px; }
  .row-2 { top: 386px; }
  .row-3 { top: 712px; }

  .heading {
    position: absolute;
    font-family: "Archivo Black", "Arial Black", sans-serif;
    color: var(--navy);
    font-size: 31px;
    letter-spacing: 1px;
    line-height: 1;
  }

  .brand-tag {
    position: absolute;
    display: flex; align-items: center; gap: 4px;
    font-family: "Arimo", Arial, sans-serif; font-weight: 700;
    color: var(--red);
  }
  .brand-tag .dot { border-radius: 50%; background: var(--navy); flex: none; }
  .brand-tag.small { right: 10px; bottom: 8px; font-size: 8px; }
  .brand-tag.small .dot { width: 14px; height: 14px; }
  .brand-tag.large { font-size: 26px; gap: 10px; color: var(--white); }
  .brand-tag.large .dot { width: 56px; height: 56px; background: var(--red); border: 3px solid var(--white); }

  /* Welcome */
  .welcome { background: var(--deep); }
  .welcome .photo {
    position: absolute; inset: 0;
    background: radial-gradient(ellipse at 75% 40%, #1c3fbf 0%, #0b24a0 35%, #061266 70%, #030a3a 100%);
  }
  .welcome .brand-tag.large { left: 32px; top: 30px; }
  .welcome .title-band {
    position: absolute; left: 30px; top: 165px; width: 285px; height: 58px;
    background: var(--navy);
    color: var(--white);
    font-family: "Arimo", Arial, sans-serif; font-weight: 700;
    font-size: 50px; line-height: 58px; padding-left: 16px; letter-spacing: 1px;
  }
  .welcome .intro {
    position: absolute; left: 33px; top: 241px; width: 490px;
    color: var(--white); font-size: 11.5px; line-height: 19px;
  }

  /* Questions */
  .questions .heading { left: 23px; top: 25px; }
  .pill {
    position: absolute; width: 246px; height: 40px;
    border: 1.3px solid var(--pill-line); border-radius: 20px;
    padding: 0 34px 0 22px;
  }
  .pill .q { font-size: 10px; font-weight: 700; color: var(--ink); line-height: 38px; white-space: nowrap; }
  .pill .toggle {
    position: absolute; right: 4px; top: 8px; width: 24px; height: 24px;
    border-radius: 50%; background: var(--red);
  }
  .pill .toggle::before, .pill .toggle.plus::after {
    content: ""; position: absolute; background: var(--white);
    left: 7px; top: 11px; width: 10px; height: 2px;
  }
  .pill .toggle.plus::after { left: 11px; top: 7px; width: 2px; height: 10px; }
  .pill.open { height: 90px; }
  .pill .answer {
    width: 212px; font-size: 7.4px; color: #555; line-height: 14.5px;
    margin-top: 0;
  }
  .p-l { left: 23px; } .p-r { left: 281px; }
  .r1 { top: 79px; } .r2 { top: 129px; } .r3 { top: 179px; } .r4 { top: 229px; }

  /* About */
  .about .heading { left: 25px; top: 41px; }
  .about .copy {
    position: absolute; left: 25px; top: 92px; width: 252px;
    font-size: 11.8px; line-height: 19.5px; color: var(--body);
  }
  .about .emblem {
    position: absolute; left: 285px; top: 32px; width: 252px; height: 252px;
    border-radius: 50%;
    background: radial-gradient(circle at 50% 45%, #5a0d22 0%, #1a1f5a 45%, var(--deep) 75%);
    border: 10px solid var(--deep);
    box-shadow: inset 0 0 0 4px var(--white);
    display: flex; align-items: center; justify-content: center;
    font-weight: 700; font-size: 24px; color: var(--white);
  }

  /* Graphs */
  .graphs .heading { left: 25px; top: 29px; }
  .graphs .lede {
    position: absolute; left: 216px; top: 27px; width: 320px;
    font-size: 11px; line-height: 19.3px; color: var(--body);
  }
  .graphs svg.chart { position: absolute; left: 0; top: 0; }
  .graphs .axis-label { font-family: "Oswald", sans-serif; font-size: 7px; fill: var(--navy); }
  .graphs .year-label { font-family: "Oswald", sans-serif; font-size: 10.5px; fill: var(--navy); }

  /* Two columns */
  .content .heading { left: 24px; top: 40px; }
  .content .column {
    position: absolute; top: 97px; width: 242px;
    font-size: 11px; line-height: 18.2px; color: var(--body);
  }
  .content .col-a { left: 23px; } .content .col-b { left: 295px; }

  /* Thank you */
  .thanks .photo {
    position: absolute; left: 0; top: 0; width: 547px; height: 214px;
    background: radial-gradient(ellipse at 55% 75%, #1f8fa8 0%, #10505f 40%, #0c2a33 75%, #0a1a20 100%);
  }
  .thanks .brand-tag.large { right: 24px; top: 20px; font-size: 22px; }
  .thanks .brand-tag.large .dot { width: 50px; height: 50px; }
  .thanks .band {
    position: absolute; left: 0; top: 214px; width: 547px; height: 93px;
    background: var(--navy);
    color: var(--white);
    font-family: "Archivo Black", "Arial Black", sans-serif;
    font-size: 66px; line-height: 93px; text-align: center; letter-spacing: 1px;
  }
</style>
</head>
<body>

<section class="slide welcome col-left row-1">
  <div class="photo" role="img" aria-label="Dark blue photograph of server racks with glowing lines of code"></div>
  <div class="brand-tag large"><span class="dot"></span>Ledger Paladin</div>
  <div class="title-band">WELCOME</div>
  <p class="intro">Lorem ipsum dolor sit amet, consectetur adipiscing elit, sed do eiusmod tempor incididunt ut labore et dolore magasus commodo viverra maecenas accumsan lacus vel facilisis.</p>
</section>

<section class="slide questions col-right row-1">
  <h2 class="heading">QUESTIONS</h2>
  <div class="pill p-l r1"><p class="q">Sed ut perspiciatis unde omnis iste ?</p><span class="toggle plus"></span></div>
  <div class="pill p-l r2"><p class="q">Nemo enim ipsam voluptatem quia?</p><span class="toggle plus"></span></div>
  <div class="pill p-l r3 open"><p class="q">Quis autem vel eum iure reprehender?</p><span class="toggle"></span>
    <p class="answer">Lorem ipsum dolor sit amet, consectetur adipiscing elit, sed do eiusmod tempor incididunt ut labore et dolore magna aliqus ipsum suspendisse ultrices gravida.</p></div>
  <div class="pill p-r r1"><p class="q">Duis aute irure dolor in reprehenderit?</p><span class="toggle plus"></span></div>
  <div class="pill p-r r2"><p class="q">Ut enim ad minima veniauis nostrum?</p><span class="toggle plus"></span></div>
  <div class="pill p-r r3"><p class="q">Neque porro quisquam estqui?</p><span class="toggle plus"></span></div>
  <div class="pill p-r r4"><p class="q">Lorem ipsum dolor sionsectetur?</p><span class="toggle plus"></span></div>
  <div class="brand-tag small"><span class="dot"></span>Ledger Paladin</div>
</section>

<section class="slide about col-left row-2">
  <h2 class="heading">ABOUT</h2>
  <p class="copy">Lorem ipsum dolor sit amet, consectetur adipiscing elit, sed do eiusmod tempor incididunt ut labore et dolore magna aliqua enim ad minim veniam, quis nostrud exercitation ullamco laboris nisi ut aliquip ex ea commodo consequat. Duis aute irure dolor in reprehenderit in voluptate velit esse cillum dolore eu fugiat nulla pariatureur sint occaecat cupidatat non proident, sunt in culpa qui officia deserunt mollit anim id est laborum.</p>
  <div class="emblem" role="img" aria-label="Large brand emblem over a red-lit server room">Ledger Paladin</div>
  <div class="brand-tag small"><span class="dot"></span>Ledger Paladin</div>
</section>

<section class="slide graphs col-right row-2">
  <h2 class="heading">GRAPHS</h2>
  <p class="lede">Lorem ipsum dolor sit amet, consectetur adipiscing elit, sed do eiusmod tempor incididunt ut labore et dolore magna aliqua enim ad minim veniam, quis nostrud exercitation ullamco laboris nisi ut aliquip ex ea commodo consequat.</p>
  <svg class="chart" width="547" height="307" viewBox="0 0 547 307">
    <g stroke="#d6e3f0" stroke-width="0.6">
      <line x1="47" y1="119" x2="451" y2="119"/><line x1="47" y1="142" x2="451" y2="142"/>
      <line x1="47" y1="164" x2="451" y2="164"/><line x1="47" y1="187" x2="451" y2="187"/>
      <line x1="47" y1="210" x2="451" y2="210"/><line x1="47" y1="232" x2="451" y2="232"/>
      <line x1="47" y1="255" x2="451" y2="255"/>
    </g>
    <g class="axis-label" text-anchor="end">
      <text x="38" y="122">700</text><text x="38" y="145">600</text><text x="38" y="167">500</text>
      <text x="38" y="190">400</text><text x="38" y="213">300</text><text x="38" y="235">200</text>
      <text x="38" y="258">100</text>
    </g>
    <g>
      <rect x="68" y="240" width="15" height="36" fill="var(--cyan)"/>
      <rect x="83" y="199" width="15" height="77" fill="var(--bar-mid)"/>
      <rect x="98" y="167" width="15" height="109" fill="var(--bar-dark)"/>
      <rect x="146" y="174" width="15" height="102" fill="var(--cyan)"/>
      <rect x="161" y="206" width="15" height="70" fill="var(--bar-mid)"/>
      <rect x="176" y="184" width="15" height="92" fill="var(--bar-dark)"/>
      <rect x="224" y="188" width="15" height="88" fill="var(--cyan)"/>
      <rect x="239" y="147" width="15" height="129" fill="var(--bar-mid)"/>
      <rect x="254" y="212" width="15" height="64" fill="var(--bar-dark)"/>
      <rect x="302" y="168" width="15" height="108" fill="var(--cyan)"/>
      <rect x="317" y="150" width="15" height="126" fill="var(--bar-mid)"/>
      <rect x="332" y="159" width="15" height="117" fill="var(--bar-dark)"/>
      <rect x="380" y="128" width="15" height="148" fill="var(--cyan)"/>
      <rect x="395" y="144" width="15" height="132" fill="var(--bar-mid)"/>
      <rect x="410" y="234" width="15" height="42" fill="var(--bar-dark)"/>
    </g>
    <line x1="47" y1="100" x2="47" y2="276" stroke="var(--navy)" stroke-width="1.2"/>
    <line x1="47" y1="276" x2="451" y2="276" stroke="var(--navy)" stroke-width="1.2"/>
    <g class="year-label" text-anchor="middle">
      <text x="89" y="295">2016</text><text x="167" y="295">2017</text><text x="245" y="295">2018</text>
      <text x="324" y="295">2019</text><text x="403" y="295">2020</text>
    </g>
  </svg>
  <div class="brand-tag small"><span class="dot"></span>Ledger Paladin</div>
</section>

<section class="slide content col-left row-3">
  <h2 class="heading">PAGE TITLE HERE</h2>
  <p class="column col-a">Lorem ipsum dolor sit amet, consectetur adipiscing elit, sed do eiusmod tempor incididunt ut labore et dolore magna aliqua enim ad minim veniam, quis nostrud exercitation ullamco laboris nisi ut aliquip ex ea commodo consequat. Duis aute irure dolor in reprehenderit in voluptate velit esse cillum dolore eu fugiat nulla pariatureur sint occaecat cupidatat non proident, sunt in culpa qui officia deserunt mollit anim id est laborum.</p>
  <p class="column col-b">Lorem ipsum dolor sit amet, consectetur adipiscing elit, sed do eiusmod tempor incididunt ut labore et dolore magna aliqua enim ad minim veniam, quis nostrud exercitation ullamco laboris nisi ut aliquip ex ea commodo consequat. Duis aute irure dolor in reprehenderit in voluptate velit esse cillum dolore eu fugiat nulla pariatureur sint occaecat cupidatat non proident, sunt in culpa qui officia deserunt mollit anim id est laborum.</p>
  <div class="brand-tag small"><span class="dot"></span>Ledger Paladin</div>
</section>

<section class="slide thanks col-right row-3">
  <div class="photo" role="img" aria-label="Teal digital network of glowing nodes and binary digits"></div>
  <div class="brand-tag large"><span class="dot"></span>Ledger Paladin</div>
  <div class="band">THANK YOU</div>
</section>

</body>
</html>
```